Statement of Professional Excellence

Our school community has create a statement of Professional Excellence at our school (TBS = The Birchfield School at Dunmore) This will be shared internally and with candidates interviewing at our school. We'd like a branded graphic that lists in an interesting way our statements:

Professional Excellence at TBS

We honor the whole child while embracing them where they are.
We are mission-driven individuals whose dedication to our students motivates our daily work.
We bring flexible thinking to allow the needs of the students to drive the learning.
We are patient, nurturing, empathetic, and compassionate people.
We value, trust, and support each other.
We learn and we teach.
We lean into and celebrate diversity.
We build trust through genuine partnerships with families.
We are quirky, fun and proud of it.

```html
<!DOCTYPE html>
<html lang="en">
<head>
<meta charset="utf-8">
<title>Professional Excellence at TBS</title>
<link href="https://fonts.googleapis.com/css2?family=Montserrat:wght@400;500;700;800&display=swap" rel="stylesheet">
<style>
  :root {
    --green-bright: #8bc63f;
    --ink-forest: #1b4d2b;
    --teal-deep: #0f4a57;
    --white: #ffffff;
  }
  * { box-sizing: border-box; margin: 0; padding: 0; }
  html, body { width: 1075px; height: 1200px; overflow: hidden; }
  body {
    font-family: "Montserrat", Arial, sans-serif;
    display: grid;
    grid-template-columns: 537.5px 537.5px;
    grid-template-rows: 600px 600px;
  }
  .colorway { position: relative; background: var(--stage); }
  .colorway--forest { --stage: #04453a; --card: #024337; --tag: var(--green-bright); --tag-ink: var(--ink-forest); --leaf: #2f7040; --tick: var(--green-bright); --mark: #b9c6c1; }
  .colorway--slate  { --stage: #1f4353; --card: #234b57; --tag: var(--green-bright); --tag-ink: var(--ink-forest); --leaf: #3a7a45; --tick: var(--green-bright); --mark: #bcc8cb; }
  .colorway--moss   { --stage: #1b4d33; --card: #1e5a3a; --tag: var(--green-bright); --tag-ink: var(--ink-forest); --leaf: #3d8045; --tick: var(--green-bright); --mark: #c0ccc4; }
  .colorway--lime   { --stage: #76b237; --card: #7ab93b; --tag: var(--teal-deep); --tag-ink: #7cbd3d; --leaf: #4f9a40; --tick: var(--teal-deep); --mark: #d6e6c6; }

  .card {
    position: absolute;
    left: 83px; top: 67px;
    width: 363px; height: 455px;
    background: var(--card);
    box-shadow: 0 6px 22px rgba(0,0,0,0.28);
  }
  .title-tag {
    position: absolute;
    left: 22px;
    height: 36px;
    background: var(--tag);
    color: var(--tag-ink);
    font-weight: 800;
    font-size: 30px;
    line-height: 36px;
    padding-left: 8px;
    letter-spacing: 0.2px;
  }
  .title-tag--1 { top: 22px; width: 258px; }
  .title-tag--2 { top: 65px; width: 218px; }
  .title-tag--3 { top: 108px; width: 127px; }

  .leaf-art {
    position: absolute;
    left: 233px; top: 84px;
    width: 101px; height: 65px;
    background: radial-gradient(ellipse at 50% 55%, var(--leaf) 0%, var(--leaf) 45%, transparent 72%);
    border-radius: 50%;
  }
  .school-name {
    position: absolute;
    left: 14px; top: 352px;
    width: 100px;
    transform: rotate(-90deg);
    transform-origin: 0 0;
    color: var(--mark);
    font-size: 10px;
    font-weight: 500;
    line-height: 12px;
    text-transform: uppercase;
    letter-spacing: 0.4px;
  }
  .values {
    position: absolute;
    left: 79px; top: 162px;
    width: 262px;
    list-style: none;
  }
  .values li {
    position: relative;
    padding-left: 15px;
    margin-bottom: 8.4px;
    color: var(--white);
    font-size: 9.4px;
    line-height: 14.8px;
    font-weight: 500;
    letter-spacing: 0.15px;
  }
  .values li b { font-weight: 800; }
  .values .tick {
    position: absolute;
    left: 0; top: 50%;
    width: 9px; height: 8px;
    margin-top: -3px;
  }
</style>
</head>
<body>

  <!-- four colourways of the same poster -->
  <section class="colorway colorway--forest">
    <article class="card">
      <div class="title-tag title-tag--1">PROFESSIONAL</div>
      <div class="title-tag title-tag--2">EXCELLENCE</div>
      <div class="title-tag title-tag--3">AT TBS</div>
      <div class="leaf-art" role="img" aria-label="Sprig of green leaves illustration"></div>
      <div class="school-name">The Birchfield School at Dunmore</div>
      <ul class="values">
        <li><svg class="tick" viewBox="0 0 9 8"><path d="M1 4.5 L3.4 7 L8 1" fill="none" stroke="var(--tick)" stroke-width="1.2"/></svg>We <b>HONOR</b> the whole child while <b>EMBRACING</b> them where they are.</li>
        <li><svg class="tick" viewBox="0 0 9 8"><path d="M1 4.5 L3.4 7 L8 1" fill="none" stroke="var(--tick)" stroke-width="1.2"/></svg>We are <b>MISSION-DRIVEN</b> individuals whose dedi-cation to our students motivates our daily work.</li>
        <li><svg class="tick" viewBox="0 0 9 8"><path d="M1 4.5 L3.4 7 L8 1" fill="none" stroke="var(--tick)" stroke-width="1.2"/></svg>We bring <b>FLEXIBLE THINKING</b> to allow the needs of the students to drive the learning.</li>
        <li><svg class="tick" viewBox="0 0 9 8"><path d="M1 4.5 L3.4 7 L8 1" fill="none" stroke="var(--tick)" stroke-width="1.2"/></svg>We are <b>PATIENT</b>, <b>NURTURING</b>, <b>EMPATHETIC</b>, and <b>COMPASSIONATE</b> people.</li>
        <li><svg class="tick" viewBox="0 0 9 8"><path d="M1 4.5 L3.4 7 L8 1" fill="none" stroke="var(--tick)" stroke-width="1.2"/></svg>We <b>VALUE</b>, <b>TRUST</b>, and <b>SUPPORT</b> each other</li>
        <li><svg class="tick" viewBox="0 0 9 8"><path d="M1 4.5 L3.4 7 L8 1" fill="none" stroke="var(--tick)" stroke-width="1.2"/></svg>We <b>LEARN</b> and we <b>TEACH</b>.</li>
        <li><svg class="tick" viewBox="0 0 9 8"><path d="M1 4.5 L3.4 7 L8 1" fill="none" stroke="var(--tick)" stroke-width="1.2"/></svg>We lean into and celebrate <b>DIVERSITY</b>.</li>
        <li><svg class="tick" viewBox="0 0 9 8"><path d="M1 4.5 L3.4 7 L8 1" fill="none" stroke="var(--tick)" stroke-width="1.2"/></svg>We build trust through <b>GENUINE PARTNERSHIPS WITH FAMILIES</b>.</li>
        <li><svg class="tick" viewBox="0 0 9 8"><path d="M1 4.5 L3.4 7 L8 1" fill="none" stroke="var(--tick)" stroke-width="1.2"/></svg>We are <b>QUIRKY</b>, <b>FUN</b> and <b>PROUD</b> of it.</li>
      </ul>
    </article>
  </section>

  <section class="colorway colorway--slate">
    <article class="card">
      <div class="title-tag title-tag--1">PROFESSIONAL</div>
      <div class="title-tag title-tag--2">EXCELLENCE</div>
      <div class="title-tag title-tag--3">AT TBS</div>
      <div class="leaf-art" role="img" aria-label="Sprig of green leaves illustration"></div>
      <div class="school-name">The Birchfield School at Dunmore</div>
      <ul class="values">
        <li><svg class="tick" viewBox="0 0 9 8"><path d="M1 4.5 L3.4 7 L8 1" fill="none" stroke="var(--tick)" stroke-width="1.2"/></svg>We <b>HONOR</b> the whole child while <b>EMBRACING</b> them where they are.</li>
        <li><svg class="tick" viewBox="0 0 9 8"><path d="M1 4.5 L3.4 7 L8 1" fill="none" stroke="var(--tick)" stroke-width="1.2"/></svg>We are <b>MISSION-DRIVEN</b> individuals whose dedi-cation to our students motivates our daily work.</li>
        <li><svg class="tick" viewBox="0 0 9 8"><path d="M1 4.5 L3.4 7 L8 1" fill="none" stroke="var(--tick)" stroke-width="1.2"/></svg>We bring <b>FLEXIBLE THINKING</b> to allow the needs of the students to drive the learning.</li>
        <li><svg class="tick" viewBox="0 0 9 8"><path d="M1 4.5 L3.4 7 L8 1" fill="none" stroke="var(--tick)" stroke-width="1.2"/></svg>We are <b>PATIENT</b>, <b>NURTURING</b>, <b>EMPATHETIC</b>, and <b>COMPASSIONATE</b> people.</li>
        <li><svg class="tick" viewBox="0 0 9 8"><path d="M1 4.5 L3.4 7 L8 1" fill="none" stroke="var(--tick)" stroke-width="1.2"/></svg>We <b>VALUE</b>, <b>TRUST</b>, and <b>SUPPORT</b> each other</li>
        <li><svg class="tick" viewBox="0 0 9 8"><path d="M1 4.5 L3.4 7 L8 1" fill="none" stroke="var(--tick)" stroke-width="1.2"/></svg>We <b>LEARN</b> and we <b>TEACH</b>.</li>
        <li><svg class="tick" viewBox="0 0 9 8"><path d="M1 4.5 L3.4 7 L8 1" fill="none" stroke="var(--tick)" stroke-width="1.2"/></svg>We lean into and celebrate <b>DIVERSITY</b>.</li>
        <li><svg class="tick" viewBox="0 0 9 8"><path d="M1 4.5 L3.4 7 L8 1" fill="none" stroke="var(--tick)" stroke-width="1.2"/></svg>We build trust through <b>GENUINE PARTNERSHIPS WITH FAMILIES</b>.</li>
        <li><svg class="tick" viewBox="0 0 9 8"><path d="M1 4.5 L3.4 7 L8 1" fill="none" stroke="var(--tick)" stroke-width="1.2"/></svg>We are <b>QUIRKY</b>, <b>FUN</b> and <b>PROUD</b> of it.</li>
      </ul>
    </article>
  </section>

  <section class="colorway colorway--moss">
    <article class="card">
      <div class="title-tag title-tag--1">PROFESSIONAL</div>
      <div class="title-tag title-tag--2">EXCELLENCE</div>
      <div class="title-tag title-tag--3">AT TBS</div>
      <div class="leaf-art" role="img" aria-label="Sprig of green leaves illustration"></div>
      <div class="school-name">The Birchfield School at Dunmore</div>
      <ul class="values">
        <li><svg class="tick" viewBox="0 0 9 8"><path d="M1 4.5 L3.4 7 L8 1" fill="none" stroke="var(--tick)" stroke-width="1.2"/></svg>We <b>HONOR</b> the whole child while <b>EMBRACING</b> them where they are.</li>
        <li><svg class="tick" viewBox="0 0 9 8"><path d="M1 4.5 L3.4 7 L8 1" fill="none" stroke="var(--tick)" stroke-width="1.2"/></svg>We are <b>MISSION-DRIVEN</b> individuals whose dedi-cation to our students motivates our daily work.</li>
        <li><svg class="tick" viewBox="0 0 9 8"><path d="M1 4.5 L3.4 7 L8 1" fill="none" stroke="var(--tick)" stroke-width="1.2"/></svg>We bring <b>FLEXIBLE THINKING</b> to allow the needs of the students to drive the learning.</li>
        <li><svg class="tick" viewBox="0 0 9 8"><path d="M1 4.5 L3.4 7 L8 1" fill="none" stroke="var(--tick)" stroke-width="1.2"/></svg>We are <b>PATIENT</b>, <b>NURTURING</b>, <b>EMPATHETIC</b>, and <b>COMPASSIONATE</b> people.</li>
        <li><svg class="tick" viewBox="0 0 9 8"><path d="M1 4.5 L3.4 7 L8 1" fill="none" stroke="var(--tick)" stroke-width="1.2"/></svg>We <b>VALUE</b>, <b>TRUST</b>, and <b>SUPPORT</b> each other</li>
        <li><svg class="tick" viewBox="0 0 9 8"><path d="M1 4.5 L3.4 7 L8 1" fill="none" stroke="var(--tick)" stroke-width="1.2"/></svg>We <b>LEARN</b> and we <b>TEACH</b>.</li>
        <li><svg class="tick" viewBox="0 0 9 8"><path d="M1 4.5 L3.4 7 L8 1" fill="none" stroke="var(--tick)" stroke-width="1.2"/></svg>We lean into and celebrate <b>DIVERSITY</b>.</li>
        <li><svg class="tick" viewBox="0 0 9 8"><path d="M1 4.5 L3.4 7 L8 1" fill="none" stroke="var(--tick)" stroke-width="1.2"/></svg>We build trust through <b>GENUINE PARTNERSHIPS WITH FAMILIES</b>.</li>
        <li><svg class="tick" viewBox="0 0 9 8"><path d="M1 4.5 L3.4 7 L8 1" fill="none" stroke="var(--tick)" stroke-width="1.2"/></svg>We are <b>QUIRKY</b>, <b>FUN</b> and <b>PROUD</b> of it.</li>
      </ul>
    </article>
  </section>

  <section class="colorway colorway--lime">
    <article class="card">
      <div class="title-tag title-tag--1">PROFESSIONAL</div>
      <div class="title-tag title-tag--2">EXCELLENCE</div>
      <div class="title-tag title-tag--3">AT TBS</div>
      <div class="leaf-art" role="img" aria-label="Sprig of green leaves illustration"></div>
      <div class="school-name">The Birchfield School at Dunmore</div>
      <ul class="values">
        <li><svg class="tick" viewBox="0 0 9 8"><path d="M1 4.5 L3.4 7 L8 1" fill="none" stroke="var(--tick)" stroke-width="1.2"/></svg>We <b>HONOR</b> the whole child while <b>EMBRACING</b> them where they are.</li>
        <li><svg class="tick" viewBox="0 0 9 8"><path d="M1 4.5 L3.4 7 L8 1" fill="none" stroke="var(--tick)" stroke-width="1.2"/></svg>We are <b>MISSION-DRIVEN</b> individuals whose dedi-cation to our students motivates our daily work.</li>
        <li><svg class="tick" viewBox="0 0 9 8"><path d="M1 4.5 L3.4 7 L8 1" fill="none" stroke="var(--tick)" stroke-width="1.2"/></svg>We bring <b>FLEXIBLE THINKING</b> to allow the needs of the students to drive the learning.</li>
        <li><svg class="tick" viewBox="0 0 9 8"><path d="M1 4.5 L3.4 7 L8 1" fill="none" stroke="var(--tick)" stroke-width="1.2"/></svg>We are <b>PATIENT</b>, <b>NURTURING</b>, <b>EMPATHETIC</b>, and <b>COMPASSIONATE</b> people.</li>
        <li><svg class="tick" viewBox="0 0 9 8"><path d="M1 4.5 L3.4 7 L8 1" fill="none" stroke="var(--tick)" stroke-width="1.2"/></svg>We <b>VALUE</b>, <b>TRUST</b>, and <b>SUPPORT</b> each other</li>
        <li><svg class="tick" viewBox="0 0 9 8"><path d="M1 4.5 L3.4 7 L8 1" fill="none" stroke="var(--tick)" stroke-width="1.2"/></svg>We <b>LEARN</b> and we <b>TEACH</b>.</li>
        <li><svg class="tick" viewBox="0 0 9 8"><path d="M1 4.5 L3.4 7 L8 1" fill="none" stroke="var(--tick)" stroke-width="1.2"/></svg>We lean into and celebrate <b>DIVERSITY</b>.</li>
        <li><svg class="tick" viewBox="0 0 9 8"><path d="M1 4.5 L3.4 7 L8 1" fill="none" stroke="var(--tick)" stroke-width="1.2"/></svg>We build trust through <b>GENUINE PARTNERSHIPS WITH FAMILIES</b>.</li>
        <li><svg class="tick" viewBox="0 0 9 8"><path d="M1 4.5 L3.4 7 L8 1" fill="none" stroke="var(--tick)" stroke-width="1.2"/></svg>We are <b>QUIRKY</b>, <b>FUN</b> and <b>PROUD</b> of it.</li>
      </ul>
    </article>
  </section>

</body>
</html>
```